LumaWireHub full website re-design

I'm looking for a current, cool new design of my website, lumawirehub.com. We sell fiber optic cables and accessories. It hasn't been changed for over 10 years. I would like fresh ideas, not excessive pictures of cables. It has to be easy to navigate because we have over 5k products that we sell. The platform that our site is built on is Prestashop. I've attached many of our popular brands as well as some of our products so you can get an idea of what we sell. I also encourage you to go to our current website to see everything we offer. We are a high end brand and I want to give that impression. The winning designer will likely have ongoing work in the future because we will be making changes and additions to our site. Prestashop experience preferred! Be creative as you want. I would like banner images across the top as well.

Target Market(s)

Men 20-50

Industry/Entity Type

Technology

Coding

Coded - Design and coding required

Number of Pages Required

5+ page

Requirements
Must have
• https://www.vidstreamo.com/watch?v=Q4-RtPw7z2M
Should not have
• cartoons

```html
<!DOCTYPE html>
<html lang="en">
<head>
<meta charset="utf-8">
<title>LumaWireHub — Fiber Optic Cables &amp; Accessories</title>
<link href="https://fonts.googleapis.com/css2?family=Montserrat:ital,wght@0,400;0,500;0,600;0,700;1,400&display=swap" rel="stylesheet">
<style>
:root{
  --crimson:#8c1b3c;
  --crimson-deep:#6e1230;
  --ink:#1f1f1f;
  --text:#555;
  --muted:#7a7a7a;
  --line:#e6e6e6;
  --panel:#f4f4f4;
  --topbar:#141414;
  --slate:#6b6a6d;
  --star:#e8a81a;
}
*{box-sizing:border-box;margin:0;padding:0}
html,body{width:1200px;height:5046px;overflow:hidden}
body{font-family:'Montserrat',sans-serif;color:var(--ink);background:#fff;position:relative}
a{color:inherit;text-decoration:none}
.wrap{width:976px;margin:0 auto;position:relative}

/* top bar */
.topbar{height:50px;background:var(--topbar);color:#fff;font-size:15px}
.topbar .wrap{display:flex;align-items:center;height:50px;justify-content:space-between}
.topbar nav{display:flex;gap:22px}
.topbar .tools{display:flex;gap:22px;align-items:center}
.topbar .tools span{display:flex;align-items:center;gap:6px}

/* hero */
.hero{height:670px;position:relative;background:linear-gradient(100deg,#1a0f12 0%,#3a1410 25%,#2a1a3a 50%,#120e16 75%,#0b0b0e 100%);overflow:hidden}
.hero-visual{position:absolute;left:120px;top:60px;width:470px;height:610px;background:radial-gradient(ellipse at 50% 45%,#4fc7c9 0%,#2e8c90 35%,rgba(20,20,24,0) 70%)}
.hero-glow{position:absolute;inset:0;background:radial-gradient(ellipse at 8% 20%,rgba(230,110,40,.45),transparent 40%),radial-gradient(ellipse at 95% 15%,rgba(120,60,200,.4),transparent 40%)}
.header{position:absolute;top:36px;left:0;right:0}
.header .wrap{display:flex;align-items:center;justify-content:space-between}
.brand{display:flex;align-items:center;gap:12px;color:#fff;font-weight:700;font-size:34px}
.brand .dot{width:30px;height:30px;border-radius:50%;background:var(--crimson);flex:none}
.mainnav{display:flex;align-items:center;gap:22px;font-size:15px;font-weight:600;color:#fff}
.mainnav .active{color:#e43c6c}
.mainnav .cat{background:#6d6d70;padding:16px 14px}
.hero-copy{position:absolute;left:700px;top:165px;width:420px;color:#fff}
.hero-copy h1{font-size:58px;line-height:1.08;font-weight:700;letter-spacing:.5px}
.hero-copy p{font-size:20px;line-height:1.6;margin:22px 0 26px;color:#e6e6e6}
.btn{display:inline-block;background:var(--crimson);color:#fff;font-weight:600;font-size:19px;padding:18px 30px;letter-spacing:.3px}
.btn.dark{background:#1b1b1b}

/* features */
.features{height:474px;padding-top:48px}
.features .wrap{display:flex;justify-content:space-between}
.feature{width:300px;text-align:center}
.feature svg{height:110px;width:120px}
.feature h3{font-size:20px;font-weight:600;margin:14px 0 18px}
.feature p{font-size:15px;line-height:26px;color:var(--muted)}
.feature a{display:block;margin-top:16px;color:var(--crimson);font-weight:600;font-size:17px}

/* section headings */
.sec-title{text-align:center;font-size:38px;font-weight:600;letter-spacing:.5px}
.sec-title em{font-style:normal;color:var(--crimson)}

/* products */
.products{height:1072px;background:var(--panel);padding-top:68px}
.grid{display:grid;grid-template-columns:repeat(4,235px);grid-auto-rows:316px;column-gap:12px;row-gap:86px;margin-top:46px}
.card{background:#fff;height:316px;text-align:center;border:1px solid #ececec;position:relative}
.card.hover{box-shadow:0 4px 16px rgba(0,0,0,.12);height:376px;z-index:1}
.card .thumb{height:165px;margin:0 18px;background:linear-gradient(135deg,#eef2f3,#c9d3d6)}
.card .thumb.teal{background:linear-gradient(135deg,#e9f4f4,#6cc3c5)}
.card .thumb.orange{background:radial-gradient(circle,#fff 30%,#f08a3a 60%,#fff 70%)}
.card .thumb.blue{background:linear-gradient(135deg,#f3f0d0,#2e64c8)}
.card h4{font-size:17px;font-weight:500;line-height:24px;margin-top:36px;padding:0 10px}
.card .price{color:var(--crimson);font-weight:600;font-size:18px;margin-top:18px}
.card .actions{position:absolute;bottom:0;left:0;right:0;height:60px;border-top:1px solid var(--line);display:flex;justify-content:center;align-items:center;gap:30px}
.view-more{display:block;width:178px;margin:52px auto 0;text-align:center;padding:20px 0}

/* edge */
.edge{height:644px;padding-top:60px}
.edge h2{font-size:38px;line-height:50px;font-weight:700;width:450px}
.edge h2 em{font-style:normal;color:var(--crimson)}
.edge p{width:440px;font-size:15px;line-height:26.5px;color:var(--text);margin-top:36px}
.edge .btn{margin-top:36px;font-size:17px;padding:18px 24px}
.video{position:absolute;left:487px;top:28px;width:489px;height:323px;background:linear-gradient(135deg,#d8dcdd,#9aa2a6 60%,#7bbfc0)}
.video .play{position:absolute;left:212px;top:130px;width:64px;height:64px;border-radius:50%;background:rgba(30,30,30,.85)}

/* speed */
.speed{height:701px;background:linear-gradient(120deg,var(--crimson-deep),#8f1f40 50%,#7a1634);color:#fff;padding-top:64px}
.speed h2{text-align:center;font-size:38px;font-weight:600}
.tabs{display:flex;justify-content:center;gap:24px;margin-top:36px}
.tab{width:118px;height:118px;border-radius:50%;background:rgba(255,255,255,.18);display:flex;align-items:center;justify-content:center;text-align:center;font-weight:600;font-size:19px;line-height:24px}
.tab.on{background:#fff;color:var(--ink)}
.speed-item{display:flex;gap:52px;margin-top:54px}
.speed-img{width:380px;height:304px;background:linear-gradient(135deg,#fafafa,#d8cfc9)}
.speed-item h3{font-size:24px;line-height:38px;font-weight:600}
.speed-item p{font-size:15px;line-height:27px;margin:20px 0 24px;color:#f1dde3}
.speed-item .btn{font-size:17px;padding:18px 24px}

/* reviews */
.reviews{height:436px;padding-top:62px;text-align:center}
.stars{margin-top:26px;color:var(--star);font-size:28px;letter-spacing:4px}
.quote{width:820px;margin:24px auto 0;font-style:italic;font-size:19px;line-height:34px;color:var(--text)}
.reviewer{margin-top:30px;font-size:21px;font-weight:500}
.arrow{position:absolute;top:236px;font-size:34px;color:#555}

/* brands */
.brands{height:353px;padding-top:48px}
.brand-row{display:flex;justify-content:space-between;margin-top:52px}
.brand-tile{width:230px;height:109px;border:1px solid var(--line);display:flex;align-items:center;justify-content:center;font-size:30px;font-weight:600;color:#9a9a9a}
.brand-tile.on{border:4px solid #ededed;color:var(--ink)}

/* newsletter */
.newsletter{height:189px;background:var(--slate);color:#fff}
.newsletter .wrap{display:flex;align-items:center;height:189px}
.newsletter h2{font-size:38px;line-height:46px;font-weight:600;width:324px}
.newsletter h2 em{font-style:normal;color:#b41b47}
.nl-form p{font-size:15px;margin-bottom:18px}
.nl-field{display:flex;width:652px;height:58px}
.nl-field span{flex:1;background:#fff;color:#666;font-size:16px;display:flex;align-items:center;padding-left:20px}
.nl-field b{width:114px;background:var(--crimson);display:flex;align-items:center;justify-content:center;font-size:17px;font-weight:600}

/* footer */
.footer{height:457px;padding-top:62px}
.footer .cols{display:flex}
.footer .logo{width:405px;color:var(--ink);font-size:40px}
.footer h5{font-size:19px;font-weight:500;margin-bottom:26px}
.footer ul{list-style:none;font-size:15px;color:#666;line-height:33px}
.links{width:232px}
.contact li{display:flex;gap:10px;margin-bottom:14px;line-height:24px}
.contact li i{color:var(--crimson);font-style:normal}
.footer .base{position:absolute;top:305px;left:0;right:0;border-top:1px solid var(--line);padding-top:34px;font-size:15px;color:#555;display:flex;justify-content:space-between}
.social{display:flex;gap:12px;margin-top:-16px}
.social span{width:48px;height:48px;border-radius:50%;border:2px solid var(--crimson)}
</style>
</head>
<body>

<header class="topbar">
  <div class="wrap">
    <nav><a>Line Card</a><a>Gov/Edu Buyers</a><a>Resellers</a></nav>
    <div class="tools">
      <span><svg width="14" height="14" viewBox="0 0 14 14"><circle cx="6" cy="6" r="4.5" fill="none" stroke="#fff" stroke-width="2"/><path d="M9 9l4 4" stroke="#fff" stroke-width="2"/></svg>Search</span>
      <span style="margin-left:20px"><svg width="12" height="14" viewBox="0 0 12 14"><rect x="1" y="6" width="10" height="8" fill="#fff"/><path d="M3 6V4a3 3 0 016 0v2" fill="none" stroke="#fff" stroke-width="2"/></svg>Login</span>
      <span><svg width="13" height="13" viewBox="0 0 13 13"><path d="M1 12l1-4 7-7 3 3-7 7z" fill="#fff"/></svg>Register</span>
      <span style="margin-left:18px"><svg width="22" height="18" viewBox="0 0 22 18"><path d="M0 1h4l3 11h12l3-8H6" fill="none" stroke="#fff" stroke-width="2"/><circle cx="9" cy="16" r="2" fill="#fff"/><circle cx="17" cy="16" r="2" fill="#fff"/></svg></span>
    </div>
  </div>
</header>

<section class="hero">
  <div class="hero-glow"></div>
  <div class="hero-visual" role="img" aria-label="Close-up of two teal fiber optic connectors against a dark, fiery background"></div>
  <div class="header">
    <div class="wrap">
      <div class="brand"><span class="dot"></span>LumaWireHub</div>
      <nav class="mainnav">
        <a class="active">HOME</a><a>30 MIN QUOTE</a><a>CUSTOM CABLE</a><a>PURCHASING</a><a class="cat">CATEGORIES ▾</a>
      </nav>
    </div>
  </div>
  <div class="hero-copy">
    <h1>LUMAWIRE<br>HUB</h1>
    <p>We want to give every one of our customers a positive experience when they do business with us.</p>
    <a class="btn">SHOP NOW</a>
  </div>
</section>

<section class="features">
  <div class="wrap">
    <div class="feature">
      <svg viewBox="0 0 120 110"><g fill="none" stroke="#555" stroke-width="3"><path d="M18 10v40c0 20 14 20 14 0V30c0-12 12-12 12 0v40c0 14 12 14 12 0V40c0-12 12-12 12 0v50h30"/></g><rect x="12" y="6" width="12" height="14" fill="var(--crimson)"/><rect x="96" y="82" width="14" height="14" fill="var(--crimson)"/></svg>
      <h3>Express Custom Cables</h3>
      <p>LWH offers TAA Compliant and Made in the USA fiber optic cables. We can custom build any length and type of fiber you need and we'll ship the order typically within 1-2 days.</p>
      <a>MAKE YOUR CABLE</a>
    </div>
    <div class="feature">
      <svg viewBox="0 0 120 110"><path d="M60 6l32 12v26c0 22-14 36-32 44-18-8-32-22-32-44V18z" fill="none" stroke="#555" stroke-width="3"/><circle cx="60" cy="42" r="14" fill="none" stroke="var(--crimson)" stroke-width="3"/><path d="M60 34v9l6 4" stroke="var(--crimson)" stroke-width="3" fill="none"/><path d="M10 86c14-6 26-6 40 2h26c6 0 6 8 0 8H54" fill="none" stroke="#555" stroke-width="3"/></svg>
      <h3>Lifetime Warranty</h3>
      <p>We stand behind the craftsmanship of every fiber optic product we deliver. From Indoor / Outdoor, Single mode &amp; Multimode to Mode Conditioning and SFP Transceivers.</p>
      <a>LEARN MORE</a>
    </div>
    <div class="feature">
      <svg viewBox="0 0 120 110"><rect x="6" y="22" width="68" height="54" fill="none" stroke="#555" stroke-width="3"/><path d="M74 40h24l16 18v18H74" fill="none" stroke="#555" stroke-width="3"/><circle cx="28" cy="82" r="9" fill="#fff" stroke="#555" stroke-width="3"/><circle cx="92" cy="82" r="9" fill="#fff" stroke="#555" stroke-width="3"/><rect x="14" y="32" width="52" height="22" fill="none" stroke="var(--crimson)" stroke-width="3"/><text x="40" y="49" text-anchor="middle" font-family="Montserrat,sans-serif" font-weight="700" font-size="16" fill="var(--crimson)">FREE</text></svg>
      <h3>Free Ground Shipping</h3>
      <p>Quality tested, securely packages, then shipped via Free CarrierX Ground to your door step complete with test results. Free Shipping available on all LumaWireHub stock cable products,</p>
      <a>LEARN MORE</a>
    </div>
  </div>
</section>

<section class="products">
  <div class="wrap">
    <h2 class="sec-title">OUR <em>PRODUCTS</em></h2>
    <div class="grid">
      <div class="card"><div class="thumb" role="img" aria-label="Duplex LC adapter"></div><h4>LC Fiber<br>Patch Cables</h4><div class="price">$8.97</div></div>
      <div class="card hover"><div class="thumb" role="img" aria-label="Set of six ST couplers"></div><h4>6 pack ST<br>couplers</h4><div class="price">$8.97</div>
        <div class="actions"><svg width="18" height="16" viewBox="0 0 22 18"><path d="M0 1h4l3 11h12l3-8H6" fill="none" stroke="#555" stroke-width="2"/><circle cx="9" cy="16" r="2" fill="#555"/><circle cx="17" cy="16" r="2" fill="#555"/></svg><svg width="18" height="16" viewBox="0 0 18 16"><path d="M9 15L2 8a4 4 0 017-5 4 4 0 017 5z" fill="#555"/></svg><svg width="20" height="14" viewBox="0 0 20 14"><ellipse cx="10" cy="7" rx="9" ry="6" fill="none" stroke="#555" stroke-width="2"/><circle cx="10" cy="7" r="3" fill="#555"/></svg><svg width="4" height="16" viewBox="0 0 4 16"><circle cx="2" cy="2" r="2" fill="#555"/><circle cx="2" cy="8" r="2" fill="#555"/><circle cx="2" cy="14" r="2" fill="#555"/></svg></div></div>
      <div class="card"><div class="thumb teal" role="img" aria-label="LC to ST multimode duplex cable ends"></div><h4>mtr lc st mm<br>dx om4</h4><div class="price">$8.97</div></div>
      <div class="card"><div class="thumb teal" role="img" aria-label="Armored aqua OM3 duplex patch cable"></div><h4>OM3 LC LC Armored<br>Duplex Fiber Patch..</h4><div class="price">$8.97</div></div>
      <div class="card"><div class="thumb orange" role="img" aria-label="Coiled orange fiber pigtails"></div><h4>Fiber Pigtails -<br>900 Micron</h4><div class="price">$8.97</div></div>
      <div class="card"><div class="thumb teal" role="img" aria-label="MPO/MTP fan-out fiber cable"></div><h4>MPO/MTP Fiber<br>Optic Cables</h4><div class="price">$8.97</div></div>
      <div class="card"><div class="thumb blue" role="img" aria-label="Yellow single-mode cable with blue SC connectors"></div><h4>OS2 LC SC Duplex<br>Fiber Patch Cable 9/125</h4><div class="price">$8.97</div></div>
      <div class="card"><div class="thumb" role="img" aria-label="Grey Cat6 patch cable plug"></div><h4>Cat6 Patch Cable -<br>Grey</h4><div class="price">$8.97</div></div>
    </div>
    <a class="btn view-more">VIEW MORE</a>
  </div>
</section>

<section class="edge">
  <div class="wrap">
    <h2>WHAT IS THE<br><em>LUMAWIREHUB</em><br>EDGE?</h2>
    <p>We want to give every one of our customers a positive experience when they do business with us. LumaWireHub's team of industry professionals has a combined 20 years of experience in all areas of the cable and connectivity business. The company was created to give customers a convenient place to shop on-line for products to meet their connectivity needs. Due to our extensive inventory we can ship many products on a same day/next day basis.</p>
    <a class="btn">LEARN MORE</a>
    <a class="video" href="https://www.vidstreamo.com/watch?v=Q4-RtPw7z2M" role="img" aria-label="Video preview showing an aqua bend-insensitive fiber patch cable">
      <span class="play"><svg width="64" height="64" viewBox="0 0 64 64"><path d="M26 20l18 12-18 12z" fill="#fff"/></svg></span>
    </a>
  </div>
</section>

<section class="speed">
  <div class="wrap">
    <h2>WHAT IS YOUR NEED FOR SPEED ?</h2>
    <div class="tabs"><div class="tab on">FAST</div><div class="tab">STILL<br>FAST</div><div class="tab">REALLY<br>FAST</div><div class="tab">WARP<br>SPEED</div></div>
    <div class="speed-item">
      <div class="speed-img" role="img" aria-label="Beige OM1 LC duplex connector"></div>
      <div style="width:544px">
        <h3>OM1 LC LC Fiber Patch Cable |<br>1Gb Duplex 62.5/125 Multimode</h3>
        <p>OM1 LC LC Fiber Patch Cables | Duplex Veltrex 62.5/125 Multi-mode Fiber Optic Assembly. Space saving, small form factor (sff), 1.25mm ceramic ferrule LC connectors with lc duplex clips. High bandwidth 62.5um multimode fiber (mmf) cable for 1/10Gbps, high speed, low loss, data transmission.</p>
        <a class="btn dark">LEARN MORE</a>
      </div>
    </div>
  </div>
</section>

<section class="reviews">
  <div class="wrap">
    <h2 class="sec-title">CUSTOMER <em>REVIEWS</em></h2>
    <div class="stars">★★★★★</div>
    <p class="quote">" The cables arrived quickly. They were rugged and met all of our specifications. Unlike another company I had used in the past these did not fall apart and their fit up was perfect when matched with the appropriate PCB fiber device. "</p>
    <div class="reviewer">10-01-2021 by Daniel R.</div>
    <span class="arrow" style="left:16px">‹</span><span class="arrow" style="right:16px">›</span>
  </div>
</section>

<section class="brands">
  <div class="wrap">
    <h2 class="sec-title">FEATURED <em>BRANDS</em></h2>
    <div class="brand-row">
      <div class="brand-tile">SnugLine</div>
      <div class="brand-tile on">FlexTurn</div>
      <div class="brand-tile">IronSheath</div>
      <div class="brand-tile">PivotPro</div>
    </div>
  </div>
</section>

<section class="newsletter">
  <div class="wrap">
    <h2>NEWSLETTER<br><em>SIGN UP</em></h2>
    <div class="nl-form">
      <p>Signup for our newsletter and receive great deals on our products.</p>
      <div class="nl-field"><span>Enter Your Email Address</span><b>SIGN UP</b></div>
    </div>
  </div>
</section>

<footer class="footer">
  <div class="wrap">
    <div class="cols">
      <div class="logo brand" style="color:var(--ink);align-items:flex-start"><span class="dot"></span>LumaWireHub</div>
      <div class="links"><h5>Quick Links</h5><ul><li>Home</li><li>About Us</li><li>Reseller</li><li>Gov/Edu Buyers</li></ul></div>
      <div><h5>Contact Information</h5>
        <ul class="contact">
          <li><i>●</i>LWH Sales Office | Warehouse ,<br>402 Meridian Ave. Suite C, VALEBROOK,<br>CA 90000 - 0000</li>
          <li><i>◔</i>Hours: 8:00am - 5:00pm / Mon-Fri</li>
          <li><i>✆</i>Call us now: (800) 555-0142</li>
          <li><i>✉</i>sales@lumawirehub.com</li>
        </ul>
      </div>
    </div>
    <div class="base"><span>Copyright © 2021 - LumaWireHub, Inc. All Right Reserved</span><div class="social"><span></span><span></span><span></span></div></div>
  </div>
</footer>

</body>
</html>
```